Journal to help kids Grades 1-5 be more creative thinkers

This is a journal for kids grades 1 - 5 where they can write, color, draw and be creative. It is designed to accompany our children's book and after-school program called Pebble Pathfinders Club. We want children to use their imagination and sense of wonder as they color, create new ideas, write stories and learn all about the creative problems solving method. We want them to learn about how to use their feelings and help others in their community. We have based this on our ORBIT method, which helps teachers teach their curriculum by engaging kids in relevant and meaningful ways and helping children of all ages learn how to think for themselves. We are a non-profit organization, so all the sales go to a scholarship fund that helps teachers pay for coaching and professional development. This journal may be used in after school programs, at home, or in classrooms. We wanted the inside to be black and white so kids feel free to make it their own but the cover should be bright and inviting. This is written and designed by Molly Drabek and Rosa Penhallow on behalf of Lantern 3 ORBIT.

Target Market(s)

Parents, schools, after school programs

Industry/Entity Type

Education

Other font styles liked:
• Fun for kids

Requirements
Must have
• Bright fun colors, our logo, easy to read font for kids
Nice to have
• Our 6 characters - but we do have them throughout book -

```html
<!DOCTYPE html>
<html lang="en">
<head>
<meta charset="utf-8">
<title>Pebble Pathfinders Journal – Cover</title>
<link href="https://fonts.googleapis.com/css2?family=Sniglet:wght@400;800&family=Lora:ital,wght@1,700&display=swap" rel="stylesheet">
<style>
  :root{
    --backdrop:#d6d6d6;
    --cover-top:#b1add8;
    --cover-mid:#9a91c6;
    --cover-bottom:#6f5f9d;
    --title-teal:#1cb0c4;
    --title-edge:#ffffff;
    --ink:#1b1b1b;
    --brand-ink:#2a3a8c;
    --apple:#f26b2a;
    --plane:#f08a3c;
    --crayon:#ef8fb1;
    --paper:#f6e9b4;
    --protractor:#5aa6d8;
    --book-green:#a8cf2e;
    --bubble:#9fd7ee;
    --hand:#f6c531;
    --ruler:#f2e27a;
    --book-stack:#4fae58;
  }
  *{margin:0;padding:0;box-sizing:border-box}
  html,body{width:1200px;height:1200px;overflow:hidden;background:var(--backdrop)}
  .stage{position:relative;width:1200px;height:1200px;display:flex;align-items:center;justify-content:center}
  .cover{
    position:relative;width:760px;height:1080px;border-radius:4px;overflow:hidden;
    background:linear-gradient(160deg,var(--cover-top) 0%,var(--cover-mid) 50%,var(--cover-bottom) 100%);
    box-shadow:0 10px 30px rgba(0,0,0,.18);
  }
  .brand{
    position:absolute;left:70px;top:90px;display:flex;align-items:center;gap:10px;
    font-family:"Sniglet",system-ui,sans-serif;font-weight:800;font-size:20px;line-height:1.1;color:var(--brand-ink);width:200px;
  }
  .brand-dot{width:34px;height:34px;border-radius:50%;background:var(--brand-ink);flex:none}
  .title{
    position:absolute;left:0;right:0;top:380px;text-align:center;
    font-family:"Sniglet",system-ui,sans-serif;font-weight:800;font-size:92px;line-height:.95;
    color:var(--title-teal);-webkit-text-stroke:3px var(--title-edge);paint-order:stroke fill;
    text-shadow:0 4px 0 var(--title-edge),0 8px 10px rgba(0,0,0,.15);
    text-transform:lowercase;
  }
  .byline{
    position:absolute;right:70px;top:860px;text-align:center;
    font-family:"Lora",Georgia,serif;font-style:italic;font-weight:700;font-size:19px;line-height:1.25;color:var(--ink);
  }
  .sticker{position:absolute;border-radius:10px}
  .sticker.apple-top{left:250px;top:24px;width:70px;height:58px;border-radius:50%;background:var(--apple)}
  .sticker.plane-top{left:400px;top:10px;width:70px;height:100px;background:var(--plane);transform:rotate(25deg)}
  .sticker.crayon-a{left:150px;top:200px;width:22px;height:90px;background:var(--crayon);transform:rotate(35deg)}
  .sticker.crayon-b{left:380px;top:210px;width:16px;height:60px;background:var(--crayon);transform:rotate(15deg)}
  .sticker.notepad-top{right:0;top:150px;width:130px;height:120px;background:var(--paper);transform:rotate(-8deg)}
  .sticker.protractor{left:-20px;top:230px;width:120px;height:70px;border-radius:70px 70px 8px 8px;background:var(--protractor)}
  .sticker.bubble-left{left:70px;top:470px;width:80px;height:80px;border-radius:50%;background:var(--bubble)}
  .sticker.bubble-right{right:-10px;top:370px;width:120px;height:80px;border-radius:60px 60px 10px 40px;background:var(--bubble)}
  .sticker.crayon-c{right:70px;top:460px;width:22px;height:80px;background:var(--crayon);transform:rotate(10deg)}
  .sticker.notebook-left{left:-10px;top:610px;width:160px;height:120px;background:var(--book-green);transform:rotate(-6deg)}
  .sticker.apple-right{right:30px;top:640px;width:80px;height:66px;border-radius:50%;background:var(--apple)}
  .sticker.plane-left{left:90px;top:770px;width:80px;height:130px;background:var(--plane);transform:rotate(30deg)}
  .sticker.books-right{right:-10px;top:800px;width:150px;height:80px;background:var(--book-stack);transform:rotate(8deg)}
  .sticker.ruler{right:20px;top:950px;width:270px;height:70px;background:var(--ruler);transform:rotate(-6deg)}
  .sticker.hand-pencil{left:30px;top:920px;width:250px;height:160px;border-radius:40px 40px 0 0;background:var(--hand)}
</style>
</head>
<body>
<main class="stage">
  <section class="cover" aria-label="Journal cover">
    <div class="sticker apple-top" role="img" aria-label="Orange apple sticker"></div>
    <div class="sticker plane-top" role="img" aria-label="Orange paper airplane sticker"></div>
    <div class="sticker crayon-a" role="img" aria-label="Pink crayon sticker"></div>
    <div class="sticker crayon-b" role="img" aria-label="Small pink crayon sticker"></div>
    <div class="sticker notepad-top" role="img" aria-label="Spiral notepad sticker"></div>
    <div class="sticker protractor" role="img" aria-label="Blue protractor sticker"></div>
    <div class="sticker bubble-left" role="img" aria-label="Magnifying glass sticker"></div>
    <div class="sticker bubble-right" role="img" aria-label="Light blue sticker"></div>
    <div class="sticker crayon-c" role="img" aria-label="Pink crayon sticker"></div>
    <div class="sticker notebook-left" role="img" aria-label="Open green notebook sticker"></div>
    <div class="sticker apple-right" role="img" aria-label="Red apple sticker"></div>
    <div class="sticker plane-left" role="img" aria-label="Orange paper airplane sticker"></div>
    <div class="sticker books-right" role="img" aria-label="Stack of books sticker"></div>
    <div class="sticker ruler" role="img" aria-label="Yellow ruler sticker"></div>
    <div class="sticker hand-pencil" role="img" aria-label="Hand holding a pencil illustration"></div>

    <div class="brand"><span class="brand-dot"></span><span>Pebble Pathfinders Club</span></div>

    <h1 class="title">pebble<br>pathfinders<br>journal</h1>

    <p class="byline">Written &amp; Designed by<br>Molly Drabek &amp; Rosa Penhallow</p>
  </section>
</main>
</body>
</html>
```